依頼詳細
焼肉とワインを提供する「焼肉ダイニング LUMA(ルーマ)」という焼肉屋の看板のデザイン製作をお願い致します。ベンチマークしているのは「さくらみなとテラス」というお店にはなりますが、こちらのお店の看板よりは、「もう少し高級感はあるが、少しカジュアルな雰囲気もある焼肉屋さんである」ということが伝わるようにして頂きたいです。表記は「YAKINIKU DINING LUMA」や「焼肉ダイニング LUMA」等、カッコ良くオシャレになっていればこだわりませんが、欲を言えば牛のイラスト等が入っていると嬉しいです。
記載項目
「YAKINIKU DINING LUMA」、「焼肉ダイニング LUMA」等
希望イメージ
シンプル 複雑
単色 カラフル
暗い 明るい
日常 高級
遊び心 厳粛
未来的 伝統的
女性的 男性的
希望する色
グレー系
納品ファイル
• イラストレーター形式 (.ai)

依頼時には決まっておらずお伝え出来ていなかった、内装の雰囲気にもあっており、色んなサイズのご提案をきめ細かにご対応頂けたので非常に気に入っております。

本当にありがとうございました!とても気に入っております。また次の店舗を出店する際にお願いできればと思っております!

```html
<!DOCTYPE html>
<html lang="ja">
<head>
<meta charset="utf-8">
<title>焼肉ダイニング LUMA 縦看板</title>
<link rel="stylesheet" href="https://fonts.googleapis.com/css2?family=Bodoni+Moda:wght@500&family=Noto+Serif+JP:wght@500&family=Noto+Sans+JP:wght@700&display=swap">
<style>
  :root {
    --paper: #ffffff;
    --ink: #4a3b35;
    --ink-faint: #ddd7d3;
    --frame: #c9c4c1;
    --label: #333333;
  }
  * { margin: 0; padding: 0; box-sizing: border-box; }
  html, body {
    width: 870px; height: 1200px; overflow: hidden;
    background: var(--paper);
  }
  .sheet { position: relative; width: 870px; height: 1200px; }

  .pattern-label {
    position: absolute; top: 14px;
    font-family: "Noto Sans JP", sans-serif;
    font-weight: 700; font-size: 15px; color: var(--label);
    white-space: nowrap; transform: translateX(-50%);
  }

  .signboard {
    position: absolute; top: 44px;
    border: 1.5px solid var(--frame);
    background: var(--paper);
    overflow: hidden;
  }
  .signboard--d { left: 40px;  width: 192px; height: 1110px; }
  .signboard--e { left: 386px; width: 232px; height: 1110px; }
  .signboard--f { left: 673px; width: 180px; height: 722px; }

  .emblem {
    position: absolute; left: 50%; transform: translateX(-50%);
    border-radius: 50%;
    border: 4px solid var(--ink);
    display: flex; align-items: center; justify-content: center;
    font-family: "Bodoni Moda", serif; font-weight: 500;
    color: var(--ink); letter-spacing: 0.04em;
  }
  .emblem--faint { border-color: var(--ink-faint); color: var(--ink-faint); }

  .tagline {
    position: absolute; left: 50%; transform: translateX(-50%);
    writing-mode: vertical-rl; text-orientation: upright;
    font-family: "Noto Serif JP", serif; font-weight: 500;
    color: var(--ink); white-space: nowrap;
    line-height: 1;
  }

  .wordmark {
    position: absolute; left: 0; right: 0;
    display: flex; flex-direction: column; align-items: center;
    font-family: "Bodoni Moda", serif; font-weight: 500;
    color: var(--ink);
  }
  .wordmark span { display: block; text-align: center; }

  /* D */
  .signboard--d .emblem--top    { top: -40px; width: 180px; height: 180px; font-size: 38px; }
  .signboard--d .emblem--bottom { top: 950px; width: 180px; height: 180px; font-size: 38px; }
  .signboard--d .tagline  { top: 215px; font-size: 42px; letter-spacing: 0.02em; }
  .signboard--d .wordmark { top: 545px; font-size: 96px; }
  .signboard--d .wordmark span { height: 96px; line-height: 96px; }

  /* E */
  .signboard--e .emblem   { top: 20px; width: 210px; height: 210px; font-size: 48px; }
  .signboard--e .tagline  { top: 258px; font-size: 48px; letter-spacing: 0.02em; }
  .signboard--e .wordmark { top: 625px; font-size: 118px; }
  .signboard--e .wordmark span { height: 112px; line-height: 112px; }

  /* F */
  .signboard--f .emblem   { top: 14px; width: 130px; height: 130px; font-size: 30px; border-width: 3px; }
  .signboard--f .tagline  { top: 160px; font-size: 32px; letter-spacing: 0.02em; }
  .signboard--f .wordmark { top: 402px; font-size: 72px; }
  .signboard--f .wordmark span { height: 70px; line-height: 70px; }
</style>
</head>
<body>
<main class="sheet">
  <p class="pattern-label" style="left:136px">縦看板・Dパターン</p>
  <p class="pattern-label" style="left:502px">縦看板・Eパターン</p>
  <p class="pattern-label" style="left:763px">縦看板・Fパターン</p>

  <section class="signboard signboard--d" aria-label="縦看板 Dパターン">
    <div class="emblem emblem--faint emblem--top">LUMA</div>
    <p class="tagline">焼肉ダイニング</p>
    <h2 class="wordmark" aria-label="LUMA"><span>L</span><span>U</span><span>M</span><span>A</span></h2>
    <div class="emblem emblem--faint emblem--bottom">LUMA</div>
  </section>

  <section class="signboard signboard--e" aria-label="縦看板 Eパターン">
    <div class="emblem">LUMA</div>
    <p class="tagline">焼肉ダイニング</p>
    <h2 class="wordmark" aria-label="LUMA"><span>L</span><span>U</span><span>M</span><span>A</span></h2>
  </section>

  <section class="signboard signboard--f" aria-label="縦看板 Fパターン">
    <div class="emblem">LUMA</div>
    <p class="tagline">焼肉ダイニング</p>
    <h2 class="wordmark" aria-label="LUMA"><span>L</span><span>U</span><span>M</span><span>A</span></h2>
  </section>
</main>
</body>
</html>
```